Fresh Start Body Quest 2017 Poster

We are having a Fresh Start, Body Quest for 2017 at our fitness studio. We need a poster design using the template attached as a reference (Only reference). I have also included our Drovelux logo to put on the poster. Please DO NOT use the graphics in the flyer as we are expecting something much much better :-)
MUST HAVES:
- Size needed 11x17 with bleeding for printing
- .PSD File Format WITH LAYERS (CS3 Compatible)*** A MUST
- Use Drovelux Bootcamps Logo
- Use Information in the attached word doc

```html
<!DOCTYPE html>
<html lang="en">
<head>
<meta charset="utf-8">
<title>Drovelux Bootcamps – Fresh Start, Body Quest</title>
<link rel="stylesheet" href="https://fonts.googleapis.com/css2?family=Roboto+Condensed:wght@300;400;700&display=swap">
<style>
  :root {
    --ink: #0b0b0c;
    --band-dark: #231f20;
    --maroon: #5a1810;
    --crimson: #8e2316;
    --copper: #b96a2a;
    --blue: #2a78c4;
    --white: #ffffff;
    --muted: #d9d4d0;
  }
  * { margin: 0; padding: 0; box-sizing: border-box; }
  html, body { width: 933px; height: 1200px; overflow: hidden; background: var(--ink); }
  body { font-family: "Roboto Condensed", Arial, sans-serif; color: var(--white); }

  .poster { position: relative; width: 933px; height: 1200px; overflow: hidden; background: var(--ink); }

  .header-band {
    position: absolute; left: 0; top: 0; width: 933px; height: 356px;
    background: radial-gradient(ellipse at 30% 0%, var(--crimson) 0%, var(--maroon) 45%, #2a0f0b 100%);
  }
  .feature-band { position: absolute; left: 0; top: 356px; width: 933px; height: 513px; background: var(--ink); }

  .athlete-photo {
    position: absolute; left: 560px; top: 40px; width: 373px; height: 828px;
    background: linear-gradient(180deg, rgba(150,100,80,0.55) 0%, rgba(120,80,62,0.6) 45%, rgba(40,30,28,0.8) 80%, rgba(11,11,12,1) 100%);
  }

  .brand-name {
    position: absolute; left: 0; top: 72px; width: 600px; text-align: center;
    font-weight: 700; font-size: 44px; letter-spacing: 1px; text-transform: uppercase; color: var(--white);
  }

  .contest-title { position: absolute; left: 0; top: 165px; width: 600px; text-align: center; }
  .contest-title .kicker { display: block; font-weight: 400; font-size: 40px; line-height: 46px; }
  .contest-title .headline { display: block; font-weight: 700; font-size: 66px; line-height: 74px; color: var(--copper); letter-spacing: 1px; }

  .pitch { position: absolute; left: 41px; top: 410px; width: 440px; }
  .pitch .lead { display: block; font-weight: 700; font-size: 47px; line-height: 56px; }
  .pitch .line { display: block; font-weight: 300; font-size: 40px; line-height: 52px; }
  .pitch .accent { display: block; font-weight: 700; font-size: 58px; line-height: 70px; color: var(--copper); }

  .duration-tab { position: absolute; left: 0; top: 683px; width: 334px; height: 127px; background: var(--copper); }
  .duration-tab .in-just { position: absolute; left: 38px; top: 18px; font-weight: 300; font-size: 48px; line-height: 48px; }
  .duration-tab .weeks { position: absolute; left: 38px; top: 64px; font-weight: 700; font-size: 52px; line-height: 52px; }
  .duration-number {
    position: absolute; left: 230px; top: 655px; font-weight: 700; font-size: 218px; line-height: 218px; color: var(--white);
  }

  .schedule {
    position: absolute; left: 0; top: 869px; width: 933px; height: 66px; background: var(--band-dark);
    display: flex; align-items: center;
  }
  .schedule .item { text-align: center; padding: 0 8px; }
  .schedule .item + .item { border-left: 1px solid var(--muted); }
  .schedule .label { display: block; font-weight: 700; font-size: 20px; line-height: 24px; }
  .schedule .value { display: block; font-weight: 400; font-size: 20px; line-height: 24px; }
  .schedule .kickoff { width: 310px; }
  .schedule .start { width: 216px; }
  .schedule .end { width: 228px; }
  .schedule .finale { width: 179px; }

  .offer { position: absolute; left: 0; top: 935px; width: 466px; height: 155px; background: var(--blue); text-align: center; padding-top: 22px; }
  .offer .small { display: block; font-weight: 400; font-size: 27px; line-height: 34px; }
  .offer .mid { display: block; font-weight: 400; font-size: 36px; line-height: 40px; }
  .offer .price { display: block; font-weight: 700; font-size: 36px; line-height: 42px; }

  .prize { position: absolute; left: 466px; top: 935px; width: 467px; height: 155px; background: var(--copper); text-align: center; padding-top: 14px; }
  .prize .amount { display: block; font-weight: 700; font-size: 64px; line-height: 72px; }
  .prize .note { display: block; font-weight: 400; font-size: 47px; line-height: 58px; }

  .footer { position: absolute; left: 0; top: 1090px; width: 933px; height: 110px; background: #000; text-align: center; padding-top: 18px; }
  .footer .label { display: block; font-weight: 400; font-size: 36px; line-height: 38px; }
  .footer .url { display: block; font-weight: 400; font-size: 31px; line-height: 38px; }
</style>
</head>
<body>
  <main class="poster">
    <div class="header-band"></div>
    <div class="feature-band"></div>

    <div class="athlete-photo" role="img" aria-label="Photo of a muscular athlete curling a barbell against a dark background"></div>

    <div class="brand-name">Drovelux Bootcamps</div>

    <h1 class="contest-title">
      <span class="kicker">FRESH START,</span>
      <span class="headline">BODY QUEST</span>
    </h1>

    <p class="pitch">
      <span class="lead">TRANSFORM</span>
      <span class="line">Your Body And Get In</span>
      <span class="line">The Best Shape Of</span>
      <span class="accent">Your Life!</span>
    </p>

    <div class="duration-tab">
      <span class="in-just">IN JUST</span>
      <span class="weeks">WEEKS</span>
    </div>
    <div class="duration-number">6</div>

    <section class="schedule">
      <div class="item kickoff"><span class="label">KICK OFF MEETING</span><span class="value">Thursday, Jan 12th at 7:30 pm</span></div>
      <div class="item start"><span class="label">START DATE</span><span class="value">Tuesday, January 17th</span></div>
      <div class="item end"><span class="label">END DATE</span><span class="value">Saturday, February 25th</span></div>
      <div class="item finale"><span class="label">FINALE PARTY</span><span class="value">March 2nd</span></div>
    </section>

    <section class="offer">
      <span class="small">6 Weeks of Training, Nutrition, and</span>
      <span class="mid">COACHING STARTING</span>
      <span class="price">AT JUST $99!</span>
    </section>

    <section class="prize">
      <span class="amount">$500 CASH</span>
      <span class="note">Prize for Winner!</span>
    </section>

    <footer class="footer">
      <span class="label">FOR MORE INFO</span>
      <span class="url">www.droveluxbootcamps.com</span>
    </footer>
  </main>
</body>
</html>
```